Project Management Consultancy needs logo, business card and stationary design

I need a logo, business card and stationary design for a start-up project management consultancy servicing clients in corporate, education, aviation, local government and construction sectors.

The business will provide professional advice to clients and our people, knowledge and experience is essentially what we sell.

Our role is to assist our clients in delivering successful construction and transition projects whilst ensuring that their needs are identified, understood and achieved.

The company is small and provides a tailor made service for our clients. We pride ourselves on being
- professional
- innovative
- collaborative
- dependable
- communicative
- confident
- bold
The logo, business card and stationary should reflect this.

Can you please include the following on the stationary as appropriate.
Address:
17 Merrowind Close
Tarrabin
NSW 2593

ABN: 42 873 306 218

I very much look forward to receiving your designs.

Gareth P.

Target Market(s)

Corporate clients such as: airports, universities, government, financial organisations, etc.

Industry/Entity Type

Management Consulting

Contact Information for Business Card

Gareth Pellow
Director
Pellow Management Consulting Pty Ltd
e. gareth.pellow@pellow-mc.example.com.au
m. +61 455 318 906

Font styles to use
Other font styles liked:
• perhaps Arial Narrow? I am open to suggestions

Requirements
Must have
• An dynamic and corporate look and feel.
Should not have
• Should not be boring.

```html
<!DOCTYPE html>
<html lang="en">
<head>
<meta charset="utf-8">
<title>Pellow Management Consulting – Business Card</title>
<link rel="stylesheet" href="https://fonts.googleapis.com/css2?family=Open+Sans:wght@400;600&display=swap">
<style>
  :root {
    --backdrop: #161616;
    --card-light: #f3f3f3;
    --brand-yellow: #e8be2c;
    --accent-yellow: #e2b42a;
    --text-grey: #4a4a4a;
    --logo-grey: #6b6b6b;
    --white: #ffffff;
  }
  * { margin: 0; padding: 0; box-sizing: border-box; }
  html, body {
    width: 1200px;
    height: 900px;
    overflow: hidden;
    background: var(--backdrop);
    font-family: "Open Sans", Arial, sans-serif;
  }
  .stage {
    position: relative;
    width: 1200px;
    height: 900px;
  }
  .card {
    position: absolute;
    top: 184px;
    height: 490px;
    border-radius: 12px;
    overflow: hidden;
  }
  .card-front {
    left: 299px;
    width: 301px;
    background: var(--card-light);
    color: var(--text-grey);
    text-align: center;
  }
  .card-back {
    left: 645px;
    width: 305px;
    background: var(--brand-yellow);
  }
  .brand {
    position: absolute;
    left: 0;
    right: 0;
    padding: 0 40px;
    display: flex;
    align-items: center;
    justify-content: center;
    gap: 10px;
  }
  .brand-square {
    width: 14px;
    height: 14px;
    flex: none;
  }
  .brand-name {
    font-weight: 600;
    font-size: 17px;
    line-height: 1.3;
    text-align: left;
    white-space: nowrap;
  }
  .card-front .brand { top: 132px; }
  .card-front .brand-square { background: var(--accent-yellow); }
  .card-front .brand-name { color: var(--logo-grey); }
  .card-back .brand { top: 335px; }
  .card-back .brand-square { background: var(--white); }
  .card-back .brand-name { color: var(--white); font-size: 19px; }

  .contact {
    position: absolute;
    top: 268px;
    left: 0;
    right: 0;
    font-size: 14.5px;
    line-height: 20px;
  }
  .person-name {
    color: var(--accent-yellow);
    font-weight: 600;
    font-size: 15.5px;
    text-transform: uppercase;
  }
  .abn { margin-top: 14px; }
  .abn-label { color: var(--accent-yellow); font-weight: 600; }
  .address { margin-top: 13px; }
  .phone { margin-top: 18px; }
  .email { font-size: 12.5px; letter-spacing: -0.1px; }
</style>
</head>
<body>
  <main class="stage">
    <section class="card card-front">
      <div class="brand">
        <span class="brand-square"></span>
        <span class="brand-name">Pellow<br>Management Consulting</span>
      </div>
      <div class="contact">
        <p class="person-name">Gareth Pellow</p>
        <p class="role">Director</p>
        <p class="abn"><span class="abn-label">ABN:</span> 42 873 306 218</p>
        <p class="address">17 Merrowind Close<br>Tarrabin NSW 2593</p>
        <p class="phone">+61 455 318 906</p>
        <p class="email">gareth.pellow@pellow-mc.example.com.au</p>
      </div>
    </section>
    <section class="card card-back">
      <div class="brand">
        <span class="brand-square"></span>
        <span class="brand-name">Pellow<br>Management Consulting</span>
      </div>
    </section>
  </main>
</body>
</html>
```